Woman owned consulting company needs an elegant and modern business card design

I need a business card design for my new consulting company, Mira Holcombe Consulting. I am looking for something that is simple and elegant, but also creative and original. You can use either version of the logo that are attached. I have also included the information that needs to be featured on the business card.

Contact Information for Business Card

Requirements
Must have
• The logo and the font type and a standard business card size. Use shades of gray/silver and or rose gold that are in the logo.
• I didn't realize that my actual logo wasn't attached. Please incorporate in the designs.
Should not have
• Colors that are different from my logo

```html
<!DOCTYPE html>
<html lang="en">
<head>
<meta charset="utf-8">
<title>Mira Holcombe Consulting — Business Cards</title>
<link href="https://fonts.googleapis.com/css2?family=Arimo:wght@400&display=swap" rel="stylesheet">
<style>
  :root {
    --backdrop: #7d7d7d;
    --card-light: #f4f4f5;
    --card-dark: #5b5b5b;
    --gold: #b8a06a;
    --ink: #5a5a5c;
    --ink-strong: #4a4a4c;
  }
  * { margin: 0; padding: 0; box-sizing: border-box; }
  html, body {
    width: 1200px;
    height: 1016px;
    overflow: hidden;
    background: var(--backdrop);
    font-family: "Arimo", Helvetica, Arial, sans-serif;
  }
  .canvas {
    position: relative;
    width: 1200px;
    height: 1016px;
  }
  .card {
    position: absolute;
    left: 332px;
    width: 549px;
    height: 314px;
    display: flex;
    flex-direction: column;
    align-items: center;
  }
  .card--front {
    top: 131px;
    background: var(--card-light);
  }
  .card--back {
    top: 514px;
    background: var(--card-dark);
    justify-content: center;
  }
  .wordmark {
    color: var(--gold);
    font-weight: 400;
    font-size: 22px;
    letter-spacing: 0.16em;
    text-align: center;
    line-height: 1.35;
    text-transform: uppercase;
  }
  .card--front .wordmark { margin-top: 62px; }
  .card-details {
    margin-top: 66px;
    text-align: center;
    color: var(--ink);
  }
  .card-details__name {
    font-size: 16px;
    color: var(--ink-strong);
    letter-spacing: 0.01em;
    margin-bottom: 16px;
  }
  .card-details__line {
    font-size: 11.5px;
    letter-spacing: 0.01em;
    line-height: 24px;
  }
  .divider { margin: 0 6px; }
</style>
</head>
<body>
<main class="canvas">
  <section class="card card--front" aria-label="Business card front">
    <div class="wordmark">Mira Holcombe<br>Consulting</div>
    <div class="card-details">
      <p class="card-details__name">MIRA HOLCOMBE<span class="divider">|</span>OWNER</p>
      <p class="card-details__line">610-555-0142<span class="divider">|</span>MIRA@MIRAHOLCOMBECONSULTING.COM</p>
      <p class="card-details__line">WWW.MIRAHOLCOMBECONSULTING.COM</p>
    </div>
  </section>

  <section class="card card--back" aria-label="Business card back">
    <div class="wordmark">Mira Holcombe<br>Consulting</div>
  </section>
</main>
</body>
</html>
```